Business cards and logo for kitchen and bath remodeling company

We want an elegant card but that calls attention something unique and when people see it they remember us. A log that we can use for our own. We are a kitchen and bathroom remodeling company. We are 3 partners staring the company we are located in seattle washington usa. We try to give the best experience and luxury look in our projects and we are looking to show that in our cards. I added a sample of a card I really like. I like the black and gold look but gray blue or green in a metallic look would look nice. I'm open to any color.

Target Market(s)

Home owners.

Industry/Entity Type

Construction

Contact Information for Business Card

Copperfern builders

Colors

Designer to choose colors to be used in the design.

Requirements
Must have
• Make a Logo
• Logo to be unique
• Name of company copperfern builders
Nice to have
• Have a good color scheme
• Front design to connect with back of card

```html
<!DOCTYPE html>
<html lang="en">
<head>
<meta charset="utf-8">
<title>Copperfern Builders — Business Card</title>
<link rel="stylesheet" href="https://fonts.googleapis.com/css2?family=Cinzel:wght@600&family=Montserrat:wght@400;500&display=swap">
<style>
  :root {
    --backdrop: #2b2b2c;
    --card-dark: #3c3c3e;
    --card-light: #ffffff;
    --gold: #c9a24a;
    --sand: #cbbd9a;
    --slate: #8a8a8d;
    --ink: #6f6f72;
  }
  * { margin: 0; padding: 0; box-sizing: border-box; }
  html, body {
    width: 1200px; height: 881px; overflow: hidden;
    background: var(--backdrop);
  }
  .canvas {
    width: 1200px; height: 881px;
    display: flex; flex-direction: column; align-items: center; justify-content: center;
    gap: 48px;
  }
  .card {
    width: 620px; height: 354px;
    border-radius: 22px;
    position: relative;
    overflow: hidden;
  }
  .card--front { background: var(--card-dark); }
  .card--back { background: var(--card-light); }

  .brand {
    font-family: "Montserrat", sans-serif;
    font-weight: 400;
    text-transform: uppercase;
    letter-spacing: 0.08em;
    line-height: 1.15;
    text-align: center;
  }
  .brand__mark {
    display: block;
    width: 34px; height: 34px;
    margin: 0 auto 18px;
    border: 2px solid currentColor;
  }
  .card--front .brand {
    color: var(--gold);
    font-size: 34px;
    position: absolute; left: 0; right: 0; top: 96px;
  }
  .card--back .brand {
    color: var(--sand);
    font-size: 30px;
    position: absolute; right: 40px; top: 92px; width: 300px;
  }

  .contact {
    position: absolute; left: 44px; top: 58px;
    font-family: "Montserrat", sans-serif;
    color: var(--ink);
  }
  .contact__name {
    font-family: "Cinzel", serif;
    font-weight: 600;
    font-size: 24px;
    color: var(--sand);
    letter-spacing: 0.04em;
  }
  .contact__role {
    font-size: 14px; font-weight: 500; letter-spacing: 0.06em;
    margin-top: 2px;
  }
  .contact__address {
    font-size: 14px; font-weight: 500; letter-spacing: 0.08em;
    line-height: 1.5; margin-top: 38px;
  }
  .contact__lines {
    list-style: none; margin-top: 30px;
    font-size: 15px; font-weight: 500; letter-spacing: 0.08em;
  }
  .contact__lines li {
    display: flex; align-items: center; gap: 12px; line-height: 1.75;
  }
  .contact__lines svg { width: 13px; height: 13px; flex: none; }
  .highlight { color: var(--sand); }
</style>
</head>
<body>
<main class="canvas">
  <section class="card card--front" aria-label="Card front">
    <div class="brand"><span class="brand__mark"></span>Copperfern<br>Builders</div>
  </section>

  <section class="card card--back" aria-label="Card back">
    <div class="contact">
      <p class="contact__name">DANIEL REYES</p>
      <p class="contact__role">Director</p>
      <p class="contact__address">418 Alder Lane<br>Renton, WA 98057</p>
      <ul class="contact__lines">
        <li>
          <svg viewBox="0 0 16 16" fill="none" stroke="var(--sand)" stroke-width="1.6" stroke-linecap="round"><path d="M4 2l2 3-1.5 1.5c1 2 2.5 3.5 4.5 4.5L10.5 9.5l3 2-1.5 2.5C7 13.5 2.5 9 2 4z"/></svg>
          206-555-0148
        </li>
        <li>
          <svg viewBox="0 0 16 16" fill="none" stroke="var(--sand)" stroke-width="1.4"><rect x="1.5" y="3.5" width="13" height="9"/><path d="M1.5 3.5L8 9l6.5-5.5"/></svg>
          info@copperfern.com
        </li>
        <li>
          <svg viewBox="0 0 16 16" fill="none" stroke="var(--sand)" stroke-width="1.3"><circle cx="8" cy="8" r="6.3"/><ellipse cx="8" cy="8" rx="2.8" ry="6.3"/><path d="M1.7 8h12.6"/></svg>
          www.<span class="highlight">copperfern</span>.com
        </li>
      </ul>
    </div>
    <div class="brand"><span class="brand__mark"></span>Copperfern<br>Builders</div>
  </section>
</main>
</body>
</html>
```